Business Card Design Project

Bold, modern, clean business card design needed. Prefer double sided with art logo on the back. Front of card with company name logo, no art.

Target Market(s)

Our consulting company supports local, state and federal law enforcement officers. Therefore the design should be clean and direct with no flash or arrogance to it.

Industry/Entity Type

Business

```html
<!DOCTYPE html>
<html lang="en">
<head>
<meta charset="UTF-8">
<title>Halden Advisory – Business Cards</title>
<link rel="stylesheet" href="https://fonts.googleapis.com/css2?family=Montserrat:wght@600&family=Open+Sans:wght@400&display=swap">
<style>
  :root {
    --backdrop: #3d3d3d;
    --card: #ffffff;
    --ink: #1a1a1a;
    --ink-soft: #333333;
    --accent: #8cc63f;
    --rule: #4a4a4a;
  }
  * { margin: 0; padding: 0; box-sizing: border-box; }
  html, body { width: 1200px; height: 750px; overflow: hidden; }
  body {
    background: var(--backdrop);
    font-family: "Open Sans", Arial, sans-serif;
    color: var(--ink);
    position: relative;
  }
  .card {
    position: absolute;
    top: 211px;
    width: 511px;
    height: 292px;
    background: var(--card);
    border-radius: 28px;
  }
  .card--back { left: 78px; }
  .card--front { left: 608px; }

  .brand {
    display: flex;
    align-items: center;
    gap: 12px;
    font-family: "Montserrat", Arial, sans-serif;
    font-weight: 600;
    color: var(--ink);
    letter-spacing: 1px;
    white-space: nowrap;
  }
  .brand__mark { background: var(--accent); flex: none; }

  .card--back .brand {
    position: absolute;
    left: 0; right: 0; top: 0; bottom: 0;
    justify-content: center;
    font-size: 32px;
  }
  .card--back .brand__mark { width: 26px; height: 26px; }

  .card--front .brand {
    position: absolute;
    left: 27px;
    top: 120px;
    font-size: 22px;
  }
  .card--front .brand__mark { width: 18px; height: 18px; }

  .person {
    position: absolute;
    right: 30px;
    top: 146px;
    text-align: right;
    line-height: 1;
  }
  .person__name { color: var(--accent); font-size: 21px; }
  .person__role { color: var(--ink-soft); font-size: 14px; margin-top: 2px; }

  .divider {
    position: absolute;
    left: 27px; right: 30px;
    top: 191px;
    height: 1px;
    background: var(--rule);
  }

  .contacts {
    position: absolute;
    left: 27px;
    top: 200px;
    list-style: none;
  }
  .contacts li {
    display: flex;
    align-items: center;
    height: 17.5px;
    font-size: 14.5px;
    color: var(--ink);
  }
  .contacts svg { width: 11px; height: 11px; margin-right: 15px; fill: var(--accent); flex: none; }

  .address {
    position: absolute;
    right: 30px;
    top: 200px;
    text-align: right;
    font-size: 14.5px;
    line-height: 18px;
    color: var(--ink);
  }
  .address__line { display: flex; justify-content: flex-end; align-items: center; }
  .address__line svg { width: 10px; height: 13px; margin-left: 8px; fill: var(--ink-soft); }
  .address__line--second { padding-right: 18px; }
</style>
</head>
<body>

<section class="card card--back" aria-label="Card back">
  <div class="brand"><span class="brand__mark"></span>HALDEN ADVISORY</div>
</section>

<section class="card card--front" aria-label="Card front">
  <div class="brand"><span class="brand__mark"></span>HALDEN ADVISORY</div>

  <div class="person">
    <div class="person__name">your name</div>
    <div class="person__role">designation</div>
  </div>

  <div class="divider"></div>

  <ul class="contacts">
    <li>
      <svg viewBox="0 0 12 12" aria-hidden="true"><path d="M1 4c0-2 2-3 5-3s5 1 5 3v1H8V4H4v1H1z M2 6h8l1 5H1z"/></svg>
      0123 456 789
    </li>
    <li>
      <svg viewBox="0 0 12 12" aria-hidden="true"><path d="M3 0h6a1 1 0 0 1 1 1v10a1 1 0 0 1-1 1H3a1 1 0 0 1-1-1V1a1 1 0 0 1 1-1zm0.5 1.5v8h5v-8z"/></svg>
      0123 456 789
    </li>
    <li>
      <svg viewBox="0 0 12 12" aria-hidden="true"><path d="M0 2h12v1L6 7 0 3z M0 4.5l6 4 6-4V10H0z"/></svg>
      youremail@mail.com
    </li>
    <li>
      <svg viewBox="0 0 12 12" aria-hidden="true"><path d="M6 0a6 6 0 1 0 0 12A6 6 0 0 0 6 0zm0 1c.8 0 1.6 1.6 1.9 4H4.1C4.4 2.6 5.2 1 6 1zM1 6.5h2.1c0 1.5.3 2.9.8 3.9A5 5 0 0 1 1 6.5zm0-1a5 5 0 0 1 2.9-3.9C3.4 2.6 3.1 4 3.1 5.5zm5 5.5c-.8 0-1.6-1.6-1.9-4.5h3.8C7.6 9.4 6.8 11 6 11zm2.1-.6c.5-1 .8-2.4.8-3.9H11a5 5 0 0 1-2.9 3.9zM8.9 5.5c0-1.5-.3-2.9-.8-3.9A5 5 0 0 1 11 5.5z"/></svg>
      www.yourwebsite.com
    </li>
  </ul>

  <address class="address" style="font-style: normal;">
    <div class="address__line">address (street address
      <svg viewBox="0 0 10 13" aria-hidden="true"><path d="M5 0a5 5 0 0 0-5 5c0 3.5 5 8 5 8s5-4.5 5-8a5 5 0 0 0-5-5zm0 7a2 2 0 1 1 0-4 2 2 0 0 1 0 4z"/></svg>
    </div>
    <div class="address__line address__line--second">suite number, city, state, zip</div>
  </address>
</section>

</body>
</html>
```